Property development business card design

New build residential property developers. I want a professional look but customer friendly so not too corporate. I'm not sure what logo will look best so open to designs with either. Thank you

Also i don't want both names on one card its 2 names for 2 different cards but with the same design.

Industry/Entity Type

Residential

Contact Information for Business Card

KRT Developments Ltd,
58 Fenwick Lane,
Ipswich,
Suffolk,
CB7 2RW

Property Research Manager
Moira Tindell

Managing Director
Derek Ashworth

```html
<!DOCTYPE html>
<html lang="en">
<head>
<meta charset="utf-8">
<title>KRT Developments – Business Card</title>
<link rel="stylesheet" href="https://fonts.googleapis.com/css2?family=Montserrat:wght@300;400;600;700&display=swap">
<style>
  :root {
    --stage: #2b2b2d;
    --paper: #ffffff;
    --paper-shade: #e9e9ea;
    --brand-blue: #1f7fc4;
    --brand-blue-deep: #1769a8;
    --accent-lime: #b7d433;
    --ink-grey: #6e6e70;
    --rule-light: rgba(255,255,255,0.45);
    --text-white: #ffffff;
  }
  * { box-sizing: border-box; margin: 0; padding: 0; }
  html, body {
    width: 1200px; height: 900px; overflow: hidden;
    background: var(--stage);
    font-family: "Montserrat", sans-serif;
  }
  .stage { position: relative; width: 1200px; height: 900px; }
  .card {
    position: absolute; left: 320px; width: 560px; height: 320px;
    background: linear-gradient(135deg, var(--paper) 40%, var(--paper-shade));
    overflow: hidden;
    box-shadow: 0 10px 30px rgba(0,0,0,0.45);
  }
  .card--front { top: 90px; }
  .card--back { top: 490px; }

  .brand {
    position: absolute; display: flex; flex-direction: column;
    align-items: center; gap: 12px;
  }
  .brand__dot { border-radius: 50%; background: var(--brand-blue); }
  .brand__name {
    font-weight: 700; color: var(--ink-grey);
    letter-spacing: 0.5px; white-space: nowrap;
  }

  .card--front .brand { left: 50%; top: 50%; transform: translate(-50%, -50%); }
  .card--front .brand__dot { width: 96px; height: 96px; }
  .card--front .brand__name { font-size: 28px; }

  .card__split { position: absolute; inset: 0; }

  .card--back .brand { left: 26px; top: 72px; width: 228px; }
  .card--back .brand__dot { width: 84px; height: 84px; }
  .card--back .brand__name { font-size: 19px; }

  .contact {
    position: absolute; left: 300px; top: 62px; width: 235px;
    color: var(--text-white); text-align: center;
  }
  .contact__name {
    font-weight: 300; font-size: 24px; color: var(--accent-lime);
    letter-spacing: 0.5px;
  }
  .contact__role {
    font-weight: 400; font-size: 9px; margin-top: 4px;
    padding-bottom: 7px; border-bottom: 1px solid var(--rule-light);
    letter-spacing: 0.3px;
  }
  .contact__address {
    display: flex; align-items: flex-start; gap: 8px;
    margin-top: 22px; padding-left: 12px; text-align: left;
    font-size: 14px; font-weight: 400; line-height: 1.35;
  }
  .contact__pin { flex: none; margin-top: 1px; }
</style>
</head>
<body>
<main class="stage">

  <section class="card card--front" aria-label="Business card front">
    <div class="brand">
      <span class="brand__dot"></span>
      <span class="brand__name">KRT DEVELOPMENTS</span>
    </div>
  </section>

  <section class="card card--back" aria-label="Business card back">
    <svg class="card__split" width="560" height="320" viewBox="0 0 560 320" aria-hidden="true">
      <defs>
        <linearGradient id="blueField" x1="0" y1="0" x2="1" y2="1">
          <stop offset="0" stop-color="#1f7fc4"/>
          <stop offset="1" stop-color="#1769a8"/>
        </linearGradient>
      </defs>
      <polygon points="175,0 560,0 560,320 355,320" fill="url(#blueField)"/>
      <line x1="178" y1="0" x2="358" y2="320" stroke="#b7d433" stroke-width="3"/>
      <line x1="170" y1="0" x2="350" y2="320" stroke="#b7d433" stroke-width="1" opacity="0.7"/>
    </svg>

    <div class="brand">
      <span class="brand__dot"></span>
      <span class="brand__name">KRT DEVELOPMENTS</span>
    </div>

    <div class="contact">
      <p class="contact__name">Moira Tindell</p>
      <p class="contact__role">Property Research Manager</p>
      <p class="contact__address">
        <svg class="contact__pin" width="16" height="16" viewBox="0 0 16 16" aria-hidden="true">
          <circle cx="8" cy="8" r="8" fill="#333"/>
          <path d="M8 3.2a3 3 0 0 0-3 3c0 2.2 3 6 3 6s3-3.8 3-6a3 3 0 0 0-3-3z" fill="#b7d433"/>
          <circle cx="8" cy="6.2" r="1.1" fill="#333"/>
        </svg>
        <span>58 Fenwick Lane, Ipswich,<br>Suffolk, CB7 2RW</span>
      </p>
    </div>
  </section>

</main>
</body>
</html>
```